The Christian Teacher Life-Cycle

Look at the Lifecyle of the Christian School.
Look at the BLT logo.
I am looking for a Christian Teacher Lifecycle that represents the slides in the PP upload.
Our website is bramblewoodlearningtrust.org.
The design should include a summary design showing all four stages, and then four slides representing each of the stages as subsets of the summary design.
When a teacher is going through the Lifecycle, they are going on their Professional Learning Journey that takes 40 years to unfold.
All five should include a copyright 2026 BLT on them.

```html
<!DOCTYPE html>
<html lang="en">
<head>
<meta charset="utf-8">
<title>Christian Teacher Lifecycle – BLT</title>
<link href="https://fonts.googleapis.com/css2?family=Montserrat:wght@500;600;700;800;900&display=swap" rel="stylesheet">
<style>
:root{
  --navy:#0f1c45;
  --green:#1f6b2a;
  --blue:#1f4fa8;
  --lime:#8bc34a;
  --ink:#1d2333;
  --muted:#5a6070;
  --rule:#d9dde4;
  --page:#ffffff;
  --frame:#e3e6eb;
}
*{box-sizing:border-box;margin:0;padding:0}
html,body{width:1200px;height:675px;overflow:hidden;background:var(--page)}
body{position:relative;font-family:"Montserrat",sans-serif;color:var(--ink)}
.panel{position:absolute;background:#fff;border:1px solid var(--frame);overflow:hidden}
.badge{position:absolute;top:0;right:0;height:22px;padding:0 12px;color:#fff;font-size:9.5px;font-weight:700;line-height:22px;border-bottom-left-radius:5px;letter-spacing:.5px}
.brand{position:absolute;display:flex;align-items:center;gap:5px;font-weight:600;color:var(--navy)}
.brand-dot{width:12px;height:12px;border-radius:50%;background:var(--green)}
.copyright{position:absolute;font-size:8px;color:var(--ink)}

/* summary */
.summary{left:11px;top:11px;width:696px;height:334px}
.summary .brand{left:22px;top:22px;font-size:20px}
.summary .brand-dot{width:18px;height:18px}
.title-small{position:absolute;left:23px;top:82px;font-size:17px;font-weight:800;color:var(--navy)}
.title-big{position:absolute;left:22px;top:100px;font-size:36px;font-weight:900;color:var(--green);letter-spacing:-.5px}
.title-sub{position:absolute;left:23px;top:146px;font-size:8.6px;font-weight:600;color:var(--muted);letter-spacing:.6px}
.intro{position:absolute;left:23px;top:177px;width:130px;font-size:9.2px;line-height:15px;font-weight:500}
.journey{position:absolute;left:320px;top:32px;width:220px;text-align:center;font-size:12.5px;font-weight:800;line-height:18.5px;color:var(--navy)}
.journey .accent{color:var(--green)}
.journey-rule{position:absolute;left:375px;top:94px;width:110px;height:1px;background:var(--navy)}
.journey-rule::after{content:"";position:absolute;left:52px;top:-2px;width:5px;height:5px;border-radius:50%;background:var(--navy)}
.timeline{position:absolute;left:0;top:0}
.stage-col{position:absolute;top:191px;width:82px;margin-left:-41px;text-align:center}
.stage-col h3{font-size:10px;font-weight:700}
.stage-col h4{font-size:7.6px;font-weight:700;line-height:11px;margin-top:3px}
.stage-col .years{font-size:7.4px;font-weight:700;margin-top:4px;color:var(--navy)}
.stage-col p{font-size:6.3px;line-height:10px;margin-top:6px;color:var(--ink)}
.c-navy{color:var(--navy)}.c-green{color:var(--green)}.c-blue{color:var(--blue)}
.footer-band{position:absolute;left:0;bottom:0;width:100%;height:31px;background:var(--navy);color:#fff;font-size:7.6px;font-weight:600;letter-spacing:.5px}
.footer-band .line{position:absolute;left:13px;top:15px;width:18px;height:1px;background:var(--lime)}
.footer-band .tagline{position:absolute;left:40px;top:6px;line-height:11px}
.footer-band .tagline span{color:var(--lime)}
.footer-band .copyright{right:25px;top:10px;color:#fff}

/* stage slides */
.stage{--accent:var(--navy)}
.stage .hero{position:absolute;width:140px;text-align:center}
.stage .hero h2{font-size:var(--h2,20px);font-weight:800;color:var(--accent)}
.stage .hero h5{font-size:var(--h5,13px);font-weight:700;line-height:var(--lh5,18px);color:var(--accent);margin-top:4px}
.stage .hero .yrs{font-size:11px;font-weight:700;color:var(--accent);margin-top:8px}
.stage .hero .yrs::after{content:"";display:block;width:26px;height:2px;background:var(--accent);margin:6px auto 0}
.stage .lead{position:absolute;font-size:9.2px;font-weight:700;line-height:14.5px;color:var(--accent)}
.stage .lead-rule{position:absolute;height:1px;background:var(--accent)}
.item{position:absolute;display:flex;align-items:flex-start}
.item-icon{flex:none;border-radius:50%;border:1px solid var(--rule);display:flex;align-items:center;justify-content:center}
.item-icon span{width:45%;height:45%;border-radius:50%;background:var(--accent)}
.item h6{font-size:8.2px;font-weight:700;color:var(--accent)}
.item p{font-size:7.6px;font-weight:500;line-height:11.5px;margin-top:2px;color:var(--ink)}
.item-rule{position:absolute;height:1px;background:var(--rule)}

.s1{left:718px;top:11px;width:471px;height:336px;--accent:var(--navy)}
.s1 .hero{left:30px;top:172px}
.s1 .lead{left:201px;top:44px;width:180px;color:var(--navy)}
.s1 .lead-rule{left:201px;top:95px;width:158px}
.s1 .item-icon{width:34px;height:34px}
.s1 .item h6,.s1 .item p{color:var(--ink)}
.s1 .item h6{font-size:8.6px}
.s1 .item{left:198px}
.s1 .item .txt{margin-left:11px;margin-top:3px}
.s1 .brand{left:20px;top:305px;font-size:17px}
.s1 .copyright{right:24px;top:320px}

.bottom{top:357px;height:308px;--h2:17.5px;--h5:11.5px;--lh5:16px}
.bottom .hero{top:149px}
.bottom .lead{top:28px;width:168px;font-size:8.6px;line-height:13px}
.bottom .lead-rule{top:74px;width:150px}
.bottom .item-icon{width:34px;height:34px}
.bottom .item .txt{margin-left:11px;margin-top:1px}
.bottom .brand{left:18px;top:272px;font-size:16px}
.bottom .copyright{right:22px;top:288px}
.s2{left:11px;width:388px;--accent:var(--green)}
.s2 .hero{left:11px}.s2 .lead,.s2 .lead-rule{left:166px}.s2 .item{left:166px}
.s3{left:410px;width:373px;--accent:var(--blue)}
.s3 .hero{left:10px}.s3 .lead,.s3 .lead-rule{left:161px}.s3 .item{left:160px}
.s4{left:794px;width:395px;--accent:var(--green)}
.s4 .hero{left:11px}.s4 .lead,.s4 .lead-rule{left:161px}.s4 .item{left:159px}
.s2 .item-icon span,.s4 .item-icon span{background:var(--green)}
.bottom .item h6{color:var(--accent)}
</style>
</head>
<body>

<!-- Summary slide -->
<section class="panel summary">
  <div class="badge" style="background:var(--navy)">1 OF 5</div>
  <div class="brand"><span class="brand-dot"></span>BLT</div>
  <div class="title-small">CHRISTIAN TEACHER</div>
  <div class="title-big">LIFECYCLE</div>
  <div class="title-sub">PROFESSIONAL LEARNING JOURNEY</div>
  <p class="intro">A 40-year journey of growth, leadership, and legacy that transforms lives for Christ and for generations to come.</p>
  <div class="journey"><span class="accent">A 40-YEAR JOURNEY</span><br>OF CALLING, GROWTH,<br>LEADERSHIP, AND LEGACY</div>
  <div class="journey-rule"></div>

  <svg class="timeline" width="696" height="200" viewBox="0 0 696 200">
    <line x1="314" y1="145" x2="360" y2="145" stroke="#0f1c45" stroke-width="1.5"/>
    <circle cx="337" cy="145" r="4" fill="#0f1c45"/>
    <line x1="418" y1="145" x2="467" y2="145" stroke="#1f6b2a" stroke-width="1.5"/>
    <circle cx="443" cy="145" r="4" fill="#1f6b2a"/>
    <line x1="525" y1="145" x2="579" y2="145" stroke="#1f4fa8" stroke-width="1.5"/>
    <circle cx="552" cy="145" r="4" fill="#1f6b2a"/>

    <circle cx="285" cy="145" r="28" fill="#fff" stroke="#0f1c45" stroke-width="3"/>
    <circle cx="285" cy="145" r="15" fill="#1f6b2a" opacity=".85" role="img" aria-label="Seedling illustration"/>
    <circle cx="285" cy="178" r="9" fill="#0f1c45"/>
    <text x="285" y="182" text-anchor="middle" font-family="Montserrat,sans-serif" font-size="11" font-weight="800" fill="#fff">1</text>

    <circle cx="389" cy="145" r="28" fill="#fff" stroke="#1f6b2a" stroke-width="3"/>
    <circle cx="389" cy="145" r="15" fill="#1f6b2a" opacity=".85" role="img" aria-label="Young plant illustration"/>
    <circle cx="389" cy="178" r="9" fill="#1f6b2a"/>
    <text x="389" y="182" text-anchor="middle" font-family="Montserrat,sans-serif" font-size="11" font-weight="800" fill="#fff">2</text>

    <circle cx="496" cy="145" r="28" fill="#fff" stroke="#1f4fa8" stroke-width="3"/>
    <circle cx="496" cy="145" r="15" fill="#1f4fa8" opacity=".85" role="img" aria-label="Group of educators illustration"/>
    <circle cx="496" cy="178" r="9" fill="#1f4fa8"/>
    <text x="496" y="182" text-anchor="middle" font-family="Montserrat,sans-serif" font-size="11" font-weight="800" fill="#fff">3</text>

    <circle cx="608" cy="145" r="28" fill="#fff" stroke="#1f6b2a" stroke-width="3"/>
    <circle cx="608" cy="145" r="15" fill="#1f6b2a" opacity=".85" role="img" aria-label="Mature tree illustration"/>
    <circle cx="608" cy="178" r="9" fill="#1f6b2a"/>
    <text x="608" y="182" text-anchor="middle" font-family="Montserrat,sans-serif" font-size="11" font-weight="800" fill="#fff">4</text>
  </svg>

  <div class="stage-col" style="left:285px"><h3 class="c-navy">STAGE 1</h3><h4 class="c-navy">CALLING &amp;<br>FOUNDATION</h4><div class="years">YEARS 1–10</div><p>Discovering God’s call and building a strong spiritual and professional foundation.</p></div>
  <div class="stage-col" style="left:389px"><h3 class="c-green">STAGE 2</h3><h4 class="c-green">GROWTH &amp;<br>DEVELOPMENT</h4><div class="years c-green">YEARS 11–20</div><p>Growing in expertise, character, and impact through continuous learning and service.</p></div>
  <div class="stage-col" style="left:496px"><h3 class="c-blue">STAGE 3</h3><h4 class="c-blue">LEADERSHIP &amp;<br>INFLUENCE</h4><div class="years">YEARS 21–30</div><p>Leading others, expanding influence, and shaping the next generation of educators.</p></div>
  <div class="stage-col" style="left:608px"><h3 class="c-green">STAGE 4</h3><h4 class="c-navy">LEGACY &amp;<br>MULTIPLICATION</h4><div class="years">YEARS 31–40</div><p>Mentoring and multiplying leaders to leave a lasting Kingdom impact.</p></div>

  <div class="footer-band">
    <div class="line"></div>
    <div class="tagline">EQUIPPING AND EMPOWERING CHRISTIAN EDUCATORS<br>FOR A LIFETIME OF <span>KINGDOM IMPACT</span></div>
    <div class="copyright">© 2026 BLT</div>
  </div>
</section>

<!-- Stage 1 -->
<section class="panel stage s1">
  <div class="badge" style="background:var(--navy)">2 OF 5</div>
  <svg style="position:absolute;left:52px;top:44px" width="96" height="120" viewBox="0 0 96 120">
    <circle cx="48" cy="48" r="44" fill="#fff" stroke="#0f1c45" stroke-width="4"/>
    <circle cx="48" cy="46" r="22" fill="#1f6b2a" opacity=".85" role="img" aria-label="Seedling illustration"/>
    <circle cx="48" cy="103" r="13" fill="#0f1c45" stroke="#fff" stroke-width="2"/>
    <text x="48" y="109" text-anchor="middle" font-family="Montserrat,sans-serif" font-size="16" font-weight="800" fill="#fff">1</text>
  </svg>
  <div class="hero"><h2>STAGE 1</h2><h5>CALLING &amp;<br>FOUNDATION</h5><div class="yrs">YEARS 1–10</div></div>
  <div class="lead">Discovering God’s call and building a strong spiritual and professional foundation.</div>
  <div class="lead-rule"></div>
  <div class="item" style="top:100px"><div class="item-icon"><span role="img" aria-label="Bible icon"></span></div><div class="txt"><h6>Deepen Faith</h6><p>Grow in Christ and His Word</p></div></div>
  <div class="item-rule" style="left:244px;top:136px;width:156px"></div>
  <div class="item" style="top:146px"><div class="item-icon"><span role="img" aria-label="Compass icon"></span></div><div class="txt"><h6>Build Foundation</h6><p>Develop core skills and confidence</p></div></div>
  <div class="item-rule" style="left:244px;top:182px;width:156px"></div>
  <div class="item" style="top:193px"><div class="item-icon"><span role="img" aria-label="Teacher icon"></span></div><div class="txt"><h6>Early Impact</h6><p>Make a difference in the classroom</p></div></div>
  <div class="item-rule" style="left:244px;top:229px;width:156px"></div>
  <div class="item" style="top:238px"><div class="item-icon"><span role="img" aria-label="Guiding hand icon"></span></div><div class="txt"><h6>Seek Guidance</h6><p>Learn from mentors</p></div></div>
  <div class="brand"><span class="brand-dot"></span>BLT</div>
  <div class="copyright">© 2026 BLT</div>
</section>

<!-- Stage 2 -->
<section class="panel stage bottom s2">
  <div class="badge" style="background:var(--green)">3 OF 5</div>
  <svg style="position:absolute;left:39px;top:35px" width="84" height="108" viewBox="0 0 84 108">
    <circle cx="42" cy="42" r="38" fill="#fff" stroke="#1f6b2a" stroke-width="4"/>
    <circle cx="42" cy="40" r="19" fill="#1f6b2a" opacity=".85" role="img" aria-label="Young plant illustration"/>
    <circle cx="42" cy="93" r="12" fill="#1f6b2a" stroke="#fff" stroke-width="2"/>
    <text x="42" y="99" text-anchor="middle" font-family="Montserrat,sans-serif" font-size="15" font-weight="800" fill="#fff">2</text>
  </svg>
  <div class="hero"><h2>STAGE 2</h2><h5>GROWTH &amp;<br>DEVELOPMENT</h5><div class="yrs">YEARS 11–20</div></div>
  <div class="lead" style="width:172px">Growing in expertise, character, and impact through continuous learning and service.</div>
  <div class="lead-rule"></div>
  <div class="item" style="top:83px"><div class="item-icon"><span role="img" aria-label="Open book icon"></span></div><div class="txt"><h6>Expand Expertise</h6><p>Strengthen teaching<br>and subject knowledge</p></div></div>
  <div class="item-rule" style="left:211px;top:124px;width:119px"></div>
  <div class="item" style="top:130px"><div class="item-icon"><span role="img" aria-label="Growth chart icon"></span></div><div class="txt"><h6>Develop Character</h6><p>Grow in integrity,<br>humility, and resilience</p></div></div>
  <div class="item-rule" style="left:211px;top:172px;width:119px"></div>
  <div class="item" style="top:178px"><div class="item-icon"><span role="img" aria-label="Team icon"></span></div><div class="txt"><h6>Increase Impact</h6><p>Take on greater<br>responsibility</p></div></div>
  <div class="item-rule" style="left:211px;top:222px;width:119px"></div>
  <div class="item" style="top:229px"><div class="item-icon"><span role="img" aria-label="Graduation cap icon"></span></div><div class="txt"><h6>Lifelong Learning</h6><p>Pursue excellence<br>continually</p></div></div>
  <div class="brand"><span class="brand-dot"></span>BLT</div>
  <div class="copyright">© 2026 BLT</div>
</section>

<!-- Stage 3 -->
<section class="panel stage bottom s3">
  <div class="badge" style="background:var(--blue)">4 OF 5</div>
  <svg style="position:absolute;left:38px;top:35px" width="84" height="108" viewBox="0 0 84 108">
    <circle cx="42" cy="42" r="38" fill="#fff" stroke="#1f4fa8" stroke-width="4"/>
    <circle cx="42" cy="42" r="19" fill="#1f4fa8" opacity=".85" role="img" aria-label="Group of educators illustration"/>
    <circle cx="42" cy="93" r="12" fill="#1f4fa8" stroke="#fff" stroke-width="2"/>
    <text x="42" y="99" text-anchor="middle" font-family="Montserrat,sans-serif" font-size="15" font-weight="800" fill="#fff">3</text>
  </svg>
  <div class="hero"><h2>STAGE 3</h2><h5>LEADERSHIP &amp;<br>INFLUENCE</h5><div class="yrs">YEARS 21–30</div></div>
  <div class="lead">Leading others, expanding influence, and shaping the next generation of educators.</div>
  <div class="lead-rule"></div>
  <div class="item" style="top:83px"><div class="item-icon"><span role="img" aria-label="Team icon"></span></div><div class="txt"><h6>Lead Others</h6><p>Inspire and equip<br>fellow educators</p></div></div>
  <div class="item-rule" style="left:204px;top:124px;width:108px"></div>
  <div class="item" style="top:130px"><div class="item-icon"><span role="img" aria-label="Gear icon"></span></div><div class="txt"><h6>Build Systems</h6><p>Improve processes<br>and school culture</p></div></div>
  <div class="item-rule" style="left:204px;top:172px;width:108px"></div>
  <div class="item" style="top:178px"><div class="item-icon"><span role="img" aria-label="Megaphone icon"></span></div><div class="txt"><h6>Expand Influence</h6><p>Serve beyond the<br>classroom</p></div></div>
  <div class="item-rule" style="left:204px;top:222px;width:108px"></div>
  <div class="item" style="top:229px"><div class="item-icon"><span role="img" aria-label="Leader icon"></span></div><div class="txt"><h6>Develop Leaders</h6><p>Mentor and raise up<br>future leaders</p></div></div>
  <div class="brand"><span class="brand-dot"></span>BLT</div>
  <div class="copyright">© 2026 BLT</div>
</section>

<!-- Stage 4 -->
<section class="panel stage bottom s4">
  <div class="badge" style="background:var(--green)">5 OF 5</div>
  <svg style="position:absolute;left:39px;top:35px" width="84" height="108" viewBox="0 0 84 108">
    <circle cx="42" cy="42" r="38" fill="#fff" stroke="#1f6b2a" stroke-width="4"/>
    <circle cx="42" cy="42" r="19" fill="#1f6b2a" opacity=".85" role="img" aria-label="Mature tree illustration"/>
    <circle cx="42" cy="93" r="12" fill="#1f6b2a" stroke="#fff" stroke-width="2"/>
    <text x="42" y="99" text-anchor="middle" font-family="Montserrat,sans-serif" font-size="15" font-weight="800" fill="#fff">4</text>
  </svg>
  <div class="hero"><h2>STAGE 4</h2><h5>LEGACY &amp;<br>MULTIPLICATION</h5><div class="yrs">YEARS 31–40</div></div>
  <div class="lead" style="width:150px">Mentoring and multiplying leaders to leave a lasting Kingdom impact.</div>
  <div class="lead-rule"></div>
  <div class="item" style="top:84px"><div class="item-icon"><span role="img" aria-label="Mentoring icon"></span></div><div class="txt"><h6>Mentor Others</h6><p>Invest in and guide<br>the next generation</p></div></div>
  <div class="item-rule" style="left:203px;top:124px;width:115px"></div>
  <div class="item" style="top:131px"><div class="item-icon"><span role="img" aria-label="Network icon"></span></div><div class="txt"><h6>Multiply Impact</h6><p>Empower others to<br>extend your reach</p></div></div>
  <div class="item-rule" style="left:203px;top:172px;width:115px"></div>
  <div class="item" style="top:179px"><div class="item-icon"><span role="img" aria-label="Globe icon"></span></div><div class="txt"><h6>Leave a Legacy</h6><p>Create lasting Kingdom<br>fruit that endures</p></div></div>
  <div class="item-rule" style="left:203px;top:222px;width:115px"></div>
  <div class="item" style="top:229px"><div class="item-icon"><span role="img" aria-label="Crown icon"></span></div><div class="txt"><h6>Glorify God</h6><p>Finish well and<br>honor His call</p></div></div>
  <div class="brand"><span class="brand-dot"></span>BLT</div>
  <div class="copyright">© 2026 BLT</div>
</section>

</body>
</html>
```